banner add for tandys sports bar and grill

need an eye catching banner design that will atract passing cars .
size will be 8 feet tall by 16feet wide

serving breakfst, lunch and dinner

best place for all PPV events

pastas,wings , ribs , gourmet burgers , salads , steaks , mexican food and seafood

phone number 418 3076

fanpage/tandyssportsbar

open from 7:00AM

Industry/Entity Type

Sports Bar

```html
<!DOCTYPE html>
<html lang="en">
<head>
<meta charset="utf-8">
<title>Tandys Sports Bar &amp; Grill – Banner</title>
<link rel="stylesheet" href="https://fonts.googleapis.com/css2?family=Great+Vibes&family=Noto+Serif:ital,wght@0,400;0,700;1,400&display=swap">
<style>
  :root {
    --red-bright: #d81f12;
    --red-mid: #c0150c;
    --red-deep: #8f0d08;
    --panel: rgba(120, 10, 6, 0.45);
    --white: #ffffff;
    --call-red: #b8140c;
    --ring-cyan: #2fc6e6;
    --ring-lime: #9ede2a;
  }
  html, body {
    margin: 0;
    padding: 0;
    width: 1200px;
    height: 600px;
    overflow: hidden;
    background: var(--red-mid);
  }
  .banner {
    position: relative;
    width: 1200px;
    height: 600px;
    overflow: hidden;
    color: var(--white);
    font-family: "Noto Serif", Georgia, serif;
    background:
      radial-gradient(ellipse 420px 160px at 420px 330px, rgba(130, 10, 5, 0.55), transparent 70%),
      radial-gradient(ellipse 300px 120px at 1050px 380px, rgba(140, 12, 6, 0.5), transparent 70%),
      radial-gradient(ellipse 500px 200px at 700px 80px, rgba(230, 50, 30, 0.35), transparent 70%),
      linear-gradient(180deg, var(--red-bright) 0%, var(--red-mid) 55%, #b0130b 100%);
  }
  .brand {
    position: absolute;
    left: 34px;
    top: 58px;
    width: 240px;
    display: flex;
    align-items: center;
    gap: 12px;
  }
  .brand-dot {
    flex: 0 0 auto;
    width: 26px;
    height: 26px;
    border-radius: 50%;
    background: var(--white);
  }
  .brand-name {
    font-weight: 700;
    font-size: 26px;
    line-height: 1.15;
    color: var(--white);
    margin: 0;
  }
  .call-badge {
    position: absolute;
    left: 866px;
    top: -70px;
    width: 400px;
    height: 145px;
    border-radius: 50%;
    background: var(--white);
  }
  .call-text {
    position: absolute;
    left: 912px;
    top: 8px;
    margin: 0;
    font-style: italic;
    font-size: 31px;
    color: var(--call-red);
    white-space: nowrap;
  }
  .tagline {
    position: absolute;
    left: 352px;
    top: 62px;
    margin: 0;
    font-family: "Great Vibes", cursive;
    font-weight: 400;
    font-size: 58px;
    letter-spacing: 2.8px;
    line-height: 1;
    white-space: nowrap;
  }
  .info-bar {
    position: absolute;
    left: 802px;
    width: 398px;
    height: 29px;
    background: var(--panel);
    font-style: italic;
    font-size: 15px;
    line-height: 29px;
    padding-left: 9px;
    box-sizing: border-box;
  }
  .info-ppv { top: 134px; }
  .info-social { top: 166px; }
  .menu-panel {
    position: absolute;
    left: 0;
    top: 213px;
    width: 340px;
    height: 272px;
  }
  .menu-list {
    position: absolute;
    left: 84px;
    top: 222px;
    margin: 0;
    padding: 0;
    list-style: none;
    font-style: italic;
    font-size: 19px;
    line-height: 30px;
  }
  .opening {
    position: absolute;
    left: 66px;
    top: 502px;
    margin: 0;
    font-style: italic;
    font-weight: 400;
    font-size: 59px;
    line-height: 1;
    white-space: nowrap;
  }
  .food-art {
    position: absolute;
    left: 0;
    top: 0;
  }
</style>
</head>
<body>
<main class="banner">
  <svg class="menu-panel" width="340" height="272" viewBox="0 0 340 272" aria-hidden="true">
    <path d="M0 0 H272 C330 70 330 200 272 272 H0 Z" fill="rgba(120,10,6,0.45)"/>
  </svg>

  <div class="brand">
    <span class="brand-dot" aria-hidden="true"></span>
    <p class="brand-name">Tandys Sports Bar &amp; Grill</p>
  </div>

  <div class="call-badge" aria-hidden="true"></div>
  <p class="call-text">Call Us : 418 3076</p>

  <h1 class="tagline">Serving breakfst, lunch and dinner</h1>

  <div class="info-bar info-ppv">Best place for all PPV events</div>
  <div class="info-bar info-social">fanpage/tandyssportsbar</div>

  <ul class="menu-list">
    <li>Pastas</li>
    <li>Wings</li>
    <li>Ribs</li>
    <li>Gourmet burgers</li>
    <li>Salads</li>
    <li>Steaks</li>
    <li>Mexican food and</li>
    <li>Seafood</li>
  </ul>

  <svg class="food-art" width="1200" height="600" viewBox="0 0 1200 600">
    <g class="ring ring-cyan" fill="none" stroke="var(--ring-cyan)">
      <circle cx="570" cy="285" r="102" stroke-width="22"/>
      <circle cx="750" cy="345" r="86" stroke-width="18"/>
    </g>
    <g class="ring ring-lime" fill="none" stroke="var(--ring-lime)">
      <circle cx="895" cy="285" r="66" stroke-width="16"/>
      <circle cx="940" cy="482" r="118" stroke-width="24"/>
    </g>
    <circle cx="570" cy="285" r="84" fill="#9a7a4e" role="img" aria-label="Photo of a gourmet burger with fries"/>
    <circle cx="750" cy="345" r="70" fill="#a5521c" role="img" aria-label="Photo of glazed chicken wings with dip"/>
    <circle cx="895" cy="285" r="52" fill="#e8c9a0" role="img" aria-label="Photo of shrimp pasta"/>
    <circle cx="940" cy="482" r="96" fill="#6b4a36" role="img" aria-label="Photo of a cheese-stuffed burger patty"/>
  </svg>

  <p class="opening">Open From 7:00 AM</p>
</main>
</body>
</html>
```